Pest control srevice Special offer

Pest control to promote our service program. 3 month pest control service for $125.00 Includes svc for ants,bees,wasps,silverfish,rats,mice,roaches. No long term contracts Our customers can purchase the service 3 months at a time as needed throughout the year. Or sign up for the full year at 425.00

Target Market(s)

Home Owners

Industry/Entity Type

Pest Control

Font styles to use
Sans Serif

Requirements
Must have
• must be relevant to pest control see our web site at brindlecovepestcontrol.example
Nice to have
• I want the post card to be laid out in a way that describes our service simple and professional. The program that we are offering really works well for our customers and makes sense they only pay for service when they are having an issue
Should not have
• I don't want pictures of insects that scare people off or unsettling to look at

```html
<!DOCTYPE html>
<html lang="en">
<head>
<meta charset="utf-8">
<title>Brindle Cove Pest Control – Service Program Postcard</title>
<link href="https://fonts.googleapis.com/css2?family=Oswald:wght@400;500;600&family=Roboto:wght@400&family=Tinos&display=swap" rel="stylesheet">
<style>
  :root {
    --artboard: #8b8b8b;
    --ink: #1c1d2e;
    --offer-red: #e3222a;
    --gold-deep: #d99e16;
    --gold: #f0bf33;
    --gold-light: #fbe27a;
    --card-yellow: #fdd54c;
    --paper: #ffffff;
    --indicia: #9a8f8f;
    --address-line: #8c6b6b;
  }
  * { margin: 0; padding: 0; box-sizing: border-box; }
  html, body { width: 971px; height: 1200px; overflow: hidden; }
  body {
    background: var(--artboard);
    position: relative;
    font-family: "Oswald", "Arial Narrow", sans-serif;
    color: var(--ink);
  }

  .postcard { position: absolute; left: 104px; width: 739px; height: 483px; overflow: hidden; }
  .postcard--front { top: 90px; }
  .postcard--back { top: 614px; background: var(--paper); }

  /* Front */
  .front-photo {
    position: absolute; inset: 0;
    background:
      radial-gradient(ellipse 260px 170px at 565px 300px, rgba(120, 78, 10, 0.55), transparent 70%),
      radial-gradient(ellipse 320px 200px at 640px 70px, #fff4b0, transparent 70%),
      radial-gradient(ellipse 420px 300px at 150px 260px, #f6cf55, transparent 75%),
      linear-gradient(160deg, var(--gold-light) 0%, var(--gold) 45%, var(--gold-deep) 100%);
  }
  .offer { position: absolute; left: 71px; top: 0; width: 380px; text-transform: uppercase; line-height: 1; }
  .offer > * { position: absolute; left: 0; white-space: nowrap; }
  .offer__term { top: 56px; font-size: 48px; font-weight: 500; letter-spacing: 0.5px; }
  .offer__label { font-size: 23px; font-weight: 400; }
  .offer__label--service { top: 98px; }
  .offer__price { font-size: 43px; font-weight: 500; }
  .offer__price--quarter { top: 120px; }
  .offer__price--year { top: 306px; }
  .price { color: var(--offer-red); }
  .offer__includes { top: 164px; font-size: 17px; line-height: 21.6px; font-weight: 400; }
  .offer__or { top: 240px; font-size: 42px; font-weight: 400; color: transparent; -webkit-text-stroke: 1.2px var(--ink); }
  .offer__label--year { top: 288px; }
  .offer__label--call { top: 366px; }
  .offer__phone { top: 388px; font-size: 44px; font-weight: 500; color: var(--offer-red); letter-spacing: 0.5px; }

  .brand {
    position: absolute; left: 592px; top: 52px; width: 106px;
    text-align: center; text-transform: uppercase;
    font-weight: 600; font-size: 20px; line-height: 20px; color: var(--ink);
  }
  .brand__sub { display: block; font-size: 20px; }

  /* Back */
  .back-message { position: absolute; left: 0; top: 0; width: 370px; height: 483px; background: var(--card-yellow); }
  .back-photo {
    position: absolute; left: 0; top: 0; width: 370px; height: 215px;
    background:
      radial-gradient(ellipse 220px 90px at 120px 40px, #f8d76a, transparent 70%),
      linear-gradient(180deg, #edbb33 0%, #f3c640 55%, var(--card-yellow) 100%);
  }
  .services { position: absolute; left: 45px; top: 62px; text-transform: uppercase; }
  .services__title { font-size: 23px; font-weight: 400; line-height: 1; margin-bottom: 9px; }
  .services__list { list-style: none; }
  .services__item {
    position: relative; padding-left: 17px;
    font-size: 17px; line-height: 28.4px; font-weight: 400;
  }
  .services__item::before {
    content: ""; position: absolute; left: 5px; top: 12px;
    width: 5px; height: 5px; border-radius: 50%; background: var(--ink);
  }
  .ant-trail { position: absolute; left: 6px; top: 254px; width: 270px; height: 229px; background: var(--card-yellow); }

  .address-side { position: absolute; left: 370px; top: 0; width: 369px; height: 483px; background: var(--paper); }
  .indicia {
    position: absolute; left: 268px; top: 36px; width: 64px; height: 58px;
    border: 1px dashed var(--indicia); outline: 2px solid #e6e1e1; outline-offset: 1px;
    padding-top: 12px;
    font-family: "Tinos", "Times New Roman", serif; font-size: 6.4px; line-height: 6.4px;
    color: var(--indicia); text-align: center; text-transform: uppercase;
  }
  .address { position: absolute; left: 64px; top: 158px; width: 242px; }
  .address__label { font-family: "Roboto", Arial, sans-serif; font-size: 8px; color: #333; margin-bottom: 18px; }
  .address__line { border-bottom: 1px dotted var(--address-line); height: 29px; }
  .address__line:first-of-type { height: 11px; }
</style>
</head>
<body>

  <section class="postcard postcard--front" aria-label="Postcard front">
    <div class="front-photo" role="img" aria-label="Close-up photograph of a honey bee working on golden honeycomb"></div>

    <div class="offer">
      <p class="offer__term">3 Month</p>
      <p class="offer__label offer__label--service">Pest Control Service</p>
      <p class="offer__price offer__price--quarter">For <span class="price">$125.00</span></p>
      <p class="offer__includes">Includes svc for<br>ants, bees, wasps, silverfish,<br>rats, mice, roaches.</p>
      <p class="offer__or">Or</p>
      <p class="offer__label offer__label--year">Sign up for the full year</p>
      <p class="offer__price offer__price--year">At <span class="price">$425.00</span></p>
      <p class="offer__label offer__label--call">Call for a free estimate!</p>
      <p class="offer__phone">800-555-0142</p>
    </div>

    <p class="brand">Brindle<br>Cove<span class="brand__sub">Pest Control</span></p>
  </section>

  <section class="postcard postcard--back" aria-label="Postcard back">
    <div class="back-message">
      <div class="back-photo" role="img" aria-label="Soft-focus photograph of golden honeycomb"></div>
      <div class="services">
        <h2 class="services__title">Our Services</h2>
        <ul class="services__list">
          <li class="services__item">Termites</li>
          <li class="services__item">Rats &amp; Mice</li>
          <li class="services__item">Carpenter Ants</li>
          <li class="services__item">Bees &amp; Wasps</li>
          <li class="services__item">Insects</li>
        </ul>
      </div>
      <div class="ant-trail" role="img" aria-label="Illustration of a trail of small black ants"></div>
    </div>

    <div class="address-side">
      <div class="indicia">Prsrt Std<br>US Postage<br>Paid<br>San Diego CA<br>Permit # 1180</div>
      <div class="address">
        <p class="address__label">To</p>
        <div class="address__line"></div>
        <div class="address__line"></div>
        <div class="address__line"></div>
        <div class="address__line"></div>
      </div>
    </div>
  </section>

</body>
</html>
```